Branding Design for KR-Reef’s Exterior & Fleet

About Us
KR-Reef is a VELQ-certified dive center on the island of Bonaire, known worldwide for its high diving standards. We specialize in Unlimited Air diving and offer a unique experience for divers with our Unlimited Air per day and Tank Cards. We offer the lowest price guarantee
What We Need
We are launching a design contest to create high-impact branding visuals for the exterior of our office and our pickup truck fleet, ensuring maximum visibility for our Unlimited Air service.
Design Locations:
1. Wall & Small Building at Our C-7 Office Location (see attached pictures and sizes (7.50 meters x 2 + 2.1 meters hight) width , the lower part 2 meter high are cars parked,so is not really usefull. )
o A striking, high-visibility design promoting Unlimited Air & Tank Cards.
o The design must be clear, bold, and immediately recognizable for passing traffic.
2. Pickup Truck Tailgate Stickers (Fleet of 150)
o A concise, attention-grabbing design that promotes Unlimited Air and tnak cards.
o Needs to be easily understood in seconds as people drive past.

Key Messages to Include:
✔ Unlimited Air – No restrictions, dive freely!
✔ Tank Cards – Easy, flexible, and cost-effective.
✔ Lowest Price Guarantee – Best deal on the island!
✔ VELQ Certified – A globally recognized diving standard.
Design Guidelines:
🎨 Incorporate the VELQ Logo – VELQ is a worldwide brand, making us instantly recognizable.
🎨 Use VELQ Colors – The color scheme should align with VELQ branding while maintaining a balance with KR-Reef’s identity.
🎨 Include the KR-Reef Logo – It must be present but should not overpower the design.
🎨 Simple & Bold – The message must be understood at a glance.
🎨 Bonaire Vibes – Use ocean-inspired elements reflecting diving culture.
🎨 Professional & Premium – KR-Reef is a trusted, high-quality dive center.
Submission Details:
• Designs must be in high-resolution formats (AI, PSD, PDF, or PNG).
• Ensure the design can be scaled for different placements.
• The winning design will be featured prominently on Bonaire, seen by thousands of divers and tourists daily!
We look forward to your creative ideas—good luck!

```html
<!DOCTYPE html>
<html lang="en">
<head>
<meta charset="utf-8">
<title>KR-Reef Exterior &amp; Fleet Branding</title>
<link rel="stylesheet" href="https://fonts.googleapis.com/css2?family=Exo+2:ital,wght@0,700;1,600;1,700;1,900&display=swap">
<style>
  :root {
    --navy: #2b3563;
    --sky: #6fcdf4;
    --orange: #f7a432;
    --white: #ffffff;
    --sea-deep: #1d5a9e;
    --sea-mid: #3f8fc4;
    --sea-light: #7cc3d9;
    --paper: #ffffff;
  }
  * { margin: 0; padding: 0; box-sizing: border-box; }
  html, body { width: 1200px; height: 800px; overflow: hidden; background: var(--paper); }
  .board { position: relative; width: 1200px; height: 800px; font-family: "Exo 2", sans-serif; }
  .label { position: absolute; font-style: italic; font-weight: 700; font-size: 12px; color: var(--navy); line-height: 1.2; }
  .piece { position: absolute; display: block; }
  .photo { position: absolute; background: linear-gradient(180deg, #cfe3f2 0%, #b9c7cf 45%, #8c8f90 75%, #c7b9a3 100%); }
  .photo--office { background: linear-gradient(180deg, #9ec7ee 0%, #d6e4ef 30%, #4a7046 50%, #2b3563 70%, #d9c8aa 100%); }
  .photo--truck { background: linear-gradient(180deg, #55575a 0%, #e6e6e6 25%, #2b3563 55%, #6fcdf4 75%, #3a3a3a 100%); }
  svg text { font-family: "Exo 2", sans-serif; }
  .t-head { font-weight: 900; font-style: italic; fill: var(--white); }
  .t-head .accent { fill: var(--sky); }
  .t-box { font-weight: 700; font-style: italic; fill: var(--navy); }
  .t-sub { font-weight: 600; font-style: italic; fill: var(--white); }
  .t-url { font-weight: 700; font-style: italic; }
  .t-brand { font-weight: 700; font-style: normal; fill: var(--white); }
  .navy { fill: var(--navy); }
  .sky { fill: var(--sky); }
  .orange { fill: var(--orange); }
</style>
</head>
<body>
<main class="board">
  <defs-holder hidden></defs-holder>
  <svg width="0" height="0" style="position:absolute">
    <defs>
      <linearGradient id="sea" x1="0" y1="0" x2="0" y2="1">
        <stop offset="0" stop-color="#4aa3c8"/>
        <stop offset="0.5" stop-color="#2f78b4"/>
        <stop offset="1" stop-color="#c79a4a"/>
      </linearGradient>
    </defs>
  </svg>

  <p class="label" style="left:617px;top:28px">Wall</p>
  <p class="label" style="left:1090px;top:77px">Office</p>
  <p class="label" style="left:323px;top:697px">Pickup Truck<br>Tailgate Stickers</p>

  <!-- Wall banner: Unlimited Air / Tank Cards -->
  <svg class="piece wall-banner" style="left:60px;top:64px" width="603" height="169" viewBox="0 0 1176 329">
    <rect width="1176" height="329" class="navy"/>
    <rect x="664" width="512" height="329" class="sky"/>
    <polygon points="545,0 664,0 664,329 400,329" fill="url(#sea)" role="img" aria-label="Underwater photos: diver, sea turtle, reef fish"/>
    <text x="50" y="92" class="t-brand" font-size="40">KR-Reef</text>
    <text class="t-head" font-size="56"><tspan x="32" y="168">ENJOY THE</tspan><tspan x="22" y="221">WATERS <tspan class="accent">OF</tspan></tspan><tspan x="20" y="272" class="accent">BONAIRE</tspan></text>
    <circle cx="28" cy="298" r="7" fill="none" stroke="#fff" stroke-width="2"/>
    <text x="40" y="306" class="t-url" font-size="21" fill="#fff">kr-reef.com</text>
    <circle cx="1137" cy="28" r="16" class="navy"/>
    <rect x="692" y="57" width="443" height="113" rx="10" class="orange"/>
    <text x="913" y="130" text-anchor="middle" class="t-box" font-size="66" textLength="420" lengthAdjust="spacingAndGlyphs">Unlimited Air</text>
    <text x="913" y="158" text-anchor="middle" class="t-sub" font-size="28">No restrictions, dive freely!</text>
    <rect x="692" y="195" width="443" height="113" rx="10" class="orange"/>
    <text x="913" y="268" text-anchor="middle" class="t-box" font-size="66" textLength="345" lengthAdjust="spacingAndGlyphs">Tank Cards</text>
    <text x="913" y="296" text-anchor="middle" class="t-sub" font-size="27" textLength="420" lengthAdjust="spacingAndGlyphs">Easy, flexible, and cost-effective.</text>
  </svg>

  <!-- Wall banner: Lowest Price / VELQ Certified -->
  <svg class="piece wall-banner" style="left:60px;top:261px" width="603" height="169" viewBox="0 0 1176 329">
    <rect width="1176" height="329" class="navy"/>
    <rect x="660" width="516" height="329" class="sky"/>
    <polygon points="460,0 660,0 660,329 315,329" fill="url(#sea)" role="img" aria-label="Underwater photos: barracuda and sea turtle"/>
    <text x="50" y="92" class="t-brand" font-size="40">KR-Reef</text>
    <text class="t-head" font-size="58"><tspan x="32" y="170">DISCOVER</tspan><tspan x="22" y="222" class="accent">SCUBA</tspan><tspan x="20" y="272">DIVING</tspan></text>
    <circle cx="28" cy="298" r="7" fill="none" stroke="#fff" stroke-width="2"/>
    <text x="40" y="306" class="t-url" font-size="21" fill="#fff">kr-reef.com</text>
    <circle cx="1137" cy="28" r="16" class="navy"/>
    <rect x="692" y="57" width="443" height="113" rx="10" class="orange"/>
    <text x="913" y="130" text-anchor="middle" class="t-box" font-size="66" textLength="400" lengthAdjust="spacingAndGlyphs">Lowest Price</text>
    <text x="900" y="158" text-anchor="middle" class="t-sub" font-size="28">Best deal on the island!</text>
    <rect x="692" y="195" width="443" height="113" rx="10" class="orange"/>
    <text x="913" y="268" text-anchor="middle" class="t-box" font-size="66" textLength="410" lengthAdjust="spacingAndGlyphs">VELQ Certified</text>
    <text x="913" y="296" text-anchor="middle" class="t-sub" font-size="24" textLength="420" lengthAdjust="spacingAndGlyphs">A globally recognized diving standard.</text>
  </svg>

  <div class="photo" style="left:63px;top:458px;width:454px;height:176px" role="img" aria-label="Photo of the banners mounted on the office wall above parked cars"></div>

  <!-- Tailgate sticker -->
  <svg class="piece tailgate" style="left:64px;top:696px" width="245" height="87" viewBox="0 0 477 170">
    <rect width="477" height="170" class="navy"/>
    <rect x="305" width="172" height="170" class="sky"/>
    <polygon points="300,0 310,0 305,170 180,170" fill="url(#sea)" role="img" aria-label="Underwater photos: turtle and divers"/>
    <polygon points="235,0 305,0 305,170 180,170" fill="url(#sea)"/>
    <text x="30" y="45" class="t-brand" font-size="24">KR-Reef</text>
    <text class="t-head" font-size="26"><tspan x="18" y="103">ENJOY THE</tspan><tspan x="14" y="127">WATERS <tspan class="accent">OF</tspan></tspan><tspan x="12" y="150" class="accent">BONAIRE</tspan></text>
    <circle cx="440" cy="18" r="10" class="navy"/>
    <rect x="305" y="45" width="148" height="38" rx="5" class="orange"/>
    <text x="379" y="70" text-anchor="middle" class="t-box" font-size="24" textLength="140" lengthAdjust="spacingAndGlyphs">Unlimited Air</text>
    <text x="379" y="80" text-anchor="middle" class="t-sub" font-size="8">No restrictions, dive freely!</text>
    <rect x="305" y="95" width="148" height="38" rx="5" class="orange"/>
    <text x="379" y="120" text-anchor="middle" class="t-box" font-size="24">Tank Cards</text>
    <text x="379" y="130" text-anchor="middle" class="t-sub" font-size="8">Easy, flexible, and cost-effective.</text>
    <circle cx="282" cy="151" r="7" fill="none" stroke="var(--navy)" stroke-width="2"/>
    <text x="295" y="159" class="t-url navy" font-size="24">kr-reef.com</text>
  </svg>

  <div class="photo photo--truck" style="left:453px;top:655px;width:197px;height:145px" role="img" aria-label="Photo of the sticker applied on a pickup truck tailgate"></div>

  <!-- Office building -->
  <svg class="piece office" style="left:756px;top:72px" width="392" height="282" viewBox="0 0 764 549">
    <polygon points="0,178 382,0 764,178 764,549 0,549" class="navy"/>
    <polygon points="490,45 764,178 764,433 370,433" class="sky"/>
    <polygon points="370,433 764,433 764,549 335,549" fill="url(#sea)" role="img" aria-label="Underwater photos: sea turtle, divers on reef, angelfish"/>
    <text x="382" y="100" text-anchor="middle" class="t-brand" font-size="38">KR-Reef</text>
    <rect x="162" y="225" width="125" height="175" class="navy" stroke="var(--sky)" stroke-width="6"/>
    <rect x="476" y="225" width="125" height="175" class="navy" stroke="var(--sky)" stroke-width="6"/>
    <circle cx="438" cy="370" r="20" class="navy"/>
    <g class="office-tabs">
      <rect x="615" y="222" width="127" height="32" rx="3" class="orange"/>
      <text x="678" y="243" text-anchor="middle" class="t-box" font-size="21" textLength="118" lengthAdjust="spacingAndGlyphs">Unlimited Air</text>
      <text x="678" y="251" text-anchor="middle" class="t-sub" font-size="7">No restrictions, dive freely!</text>
      <rect x="615" y="270" width="127" height="32" rx="3" class="orange"/>
      <text x="678" y="291" text-anchor="middle" class="t-box" font-size="21">Tank Cards</text>
      <text x="678" y="299" text-anchor="middle" class="t-sub" font-size="7">Easy, flexible, and cost-effective.</text>
      <rect x="615" y="319" width="127" height="32" rx="3" class="orange"/>
      <text x="678" y="340" text-anchor="middle" class="t-box" font-size="21">Lowest Price</text>
      <text x="678" y="348" text-anchor="middle" class="t-sub" font-size="7">Best deal on the island!</text>
      <rect x="615" y="367" width="127" height="32" rx="3" class="orange"/>
      <text x="678" y="388" text-anchor="middle" class="t-box" font-size="21" textLength="118" lengthAdjust="spacingAndGlyphs">VELQ Certified</text>
      <text x="678" y="396" text-anchor="middle" class="t-sub" font-size="6">A globally recognized diving standard.</text>
    </g>
    <circle cx="601" cy="418" r="7" fill="none" stroke="var(--navy)" stroke-width="2"/>
    <text x="614" y="426" class="t-url navy" font-size="22">kr-reef.com</text>
    <text class="t-head" font-size="41"><tspan x="48" y="455">ENJOY THE</tspan><tspan x="42" y="494">WATERS <tspan class="accent">OF</tspan></tspan><tspan x="38" y="532" class="accent">BONAIRE</tspan></text>
  </svg>

  <div class="photo photo--office" style="left:721px;top:389px;width:454px;height:341px" role="img" aria-label="Photo of the design painted on the small office building"></div>
</main>
</body>
</html>
```